LINGERIE WEBSHOP - Velora casa

We are looking for design and layout design for our webshop. We are company that sells lingerie and other connected textile products liki payamas and etc..
Our website will have approx 500 different products within 2 main catogories Woman/Man) and approx. 10 subcategories
Here is what we expect form design:
-Color pallete should be black and white (if you wish you can add some accent color)
-we want to leave feeling to customers of good quality products towards to luxury
-UX should be simple. Feel free to suggest layout
-frontpage layout, product list layout, product description layout, blog layout
-responsive design, compatible with smartphone

Target Market(s)

woman buying for themself, man buying for woman

Industry/Entity Type

Lingerie

Logo Text

VELORA CASA

Number of Pages Required

4 page

Font styles to use
Sans Serif
Decorative

Requirements
Must have
• simple UX
Nice to have
• difference for sexy/luxury lingerie and daily/cozy lingerie
Should not have
• cheap feel, unreliable

```html
<!DOCTYPE html>
<html lang="en">
<head>
<meta charset="utf-8">
<title>Velora casa — New Season Lingerie</title>
<link rel="stylesheet" href="https://fonts.googleapis.com/css2?family=Poppins:wght@400;500&family=Playfair+Display:wght@700&family=Libre+Caslon+Text:wght@400&display=swap">
<style>
  :root {
    --ink: #111111;
    --ink-soft: #2a2a2a;
    --header-bg: #f8f8f8;
    --nav-bg: #ffffff;
    --line: #8a8585;
    --dot: #b9b3b5;
    --hero-blush: #efd7da;
    --hero-mist: #f3eeef;
    --hero-wall: #ebe7ec;
    --hero-shadow: #c9c1c6;
  }
  * { box-sizing: border-box; margin: 0; padding: 0; }
  html, body { width: 1200px; height: 864px; overflow: hidden; background: var(--nav-bg); }
  body { position: relative; font-family: "Poppins", Arial, sans-serif; color: var(--ink); }

  .site-header {
    position: absolute; left: 0; top: 0; width: 1200px; height: 96px;
    background: var(--header-bg);
  }
  .brand-name {
    position: absolute; left: 0; right: 0; top: 40px; text-align: center;
    font-family: "Libre Caslon Text", Georgia, serif; font-size: 26px;
    letter-spacing: 1px; color: var(--ink); line-height: 1;
  }
  .header-actions { position: absolute; top: 27px; left: 987px; display: flex; gap: 18px; }
  .icon-button {
    position: relative; width: 40px; height: 40px; border-radius: 50%;
    border: 1px solid var(--ink); display: flex; align-items: center; justify-content: center;
  }
  .icon-badge {
    position: absolute; top: -6px; right: -8px; width: 20px; height: 20px; border-radius: 50%;
    background: var(--ink); color: #fff; font-size: 10px; font-weight: 500;
    display: flex; align-items: center; justify-content: center;
  }

  .main-nav {
    position: absolute; left: 0; top: 96px; width: 1200px; height: 56px;
    background: var(--nav-bg); display: flex; justify-content: center; align-items: center; gap: 34px;
    font-size: 13px; font-weight: 400; letter-spacing: 0.2px;
  }
  .main-nav span { display: flex; align-items: center; gap: 4px; }

  .hero {
    position: absolute; left: 0; top: 152px; width: 1200px; height: 712px; overflow: hidden;
  }
  .hero-photo {
    position: absolute; inset: 0;
    background: linear-gradient(90deg, var(--hero-blush) 0%, #f1dfe1 28%, var(--hero-mist) 40%, var(--hero-wall) 55%, var(--hero-shadow) 75%, var(--hero-wall) 100%);
  }
  .hero-copy { position: absolute; left: 119px; top: 278px; }
  .hero-title {
    font-family: "Playfair Display", Georgia, serif; font-weight: 700; font-size: 52px;
    line-height: 1; color: var(--ink); letter-spacing: 0.3px;
  }
  .hero-lede {
    margin-top: 26px; width: 400px; font-family: "Libre Caslon Text", Georgia, serif;
    font-size: 19px; line-height: 33px; color: var(--ink-soft);
  }
  .hero-button {
    margin-top: 26px; width: 145px; height: 51px; border: 1px solid var(--line); border-radius: 26px;
    display: flex; align-items: center; justify-content: center; gap: 10px;
    font-size: 13px; color: var(--ink-soft);
  }
  .slide-dots { position: absolute; left: 18px; top: 329px; display: flex; flex-direction: column; align-items: center; gap: 17px; width: 18px; }
  .slide-dot { width: 4px; height: 4px; border-radius: 50%; background: var(--dot); }
  .slide-dot.is-active {
    width: 18px; height: 18px; background: transparent; border: 1.5px solid var(--line);
    display: flex; align-items: center; justify-content: center;
  }
  .slide-dot.is-active::after { content: ""; width: 4px; height: 4px; border-radius: 50%; background: var(--ink); }
</style>
</head>
<body>
  <header class="site-header">
    <div class="brand-name">VELORA CASA</div>
    <div class="header-actions">
      <div class="icon-button">
        <svg width="15" height="14" viewBox="0 0 24 22" fill="none" stroke="#111" stroke-width="1.6"><path d="M12 20s-9-5.5-9-12a5 5 0 0 1 9-3 5 5 0 0 1 9 3c0 6.5-9 12-9 12z"/></svg>
        <span class="icon-badge">1</span>
      </div>
      <div class="icon-button">
        <svg width="16" height="15" viewBox="0 0 24 22" fill="none" stroke="#111" stroke-width="1.6"><path d="M1 2h4l3 12h12l3-9H6"/><circle cx="10" cy="19" r="1.6"/><circle cx="18" cy="19" r="1.6"/></svg>
        <span class="icon-badge">3</span>
      </div>
    </div>
  </header>

  <nav class="main-nav">
    <span>HOME</span>
    <span>WOMEN <svg width="12" height="7" viewBox="0 0 12 7" fill="none" stroke="#111" stroke-width="1"><path d="M1 1l5 5 5-5"/></svg></span>
    <span>MEN <svg width="12" height="7" viewBox="0 0 12 7" fill="none" stroke="#111" stroke-width="1"><path d="M1 1l5 5 5-5"/></svg></span>
    <span>TRENDING</span>
    <span>CONTACT</span>
  </nav>

  <section class="hero">
    <div class="hero-photo" role="img" aria-label="Model in a black bodysuit and sheer robe standing by a white door with blush pink curtains"></div>
    <div class="slide-dots">
      <span class="slide-dot"></span>
      <span class="slide-dot"></span>
      <span class="slide-dot is-active"></span>
    </div>
    <div class="hero-copy">
      <h1 class="hero-title">New Season Lingerie</h1>
      <p class="hero-lede">Wide selection of women's underwear from the new 2020 collection</p>
      <div class="hero-button">Learn More
        <svg width="14" height="12" viewBox="0 0 14 12" fill="none" stroke="#2a2a2a" stroke-width="1.3"><path d="M1 6h12M8 1l5 5-5 5"/></svg>
      </div>
    </div>
  </section>
</body>
</html>
```